Redesign our business card for more impact

We want to completely replace the back design of our card, and refresh or even change the front entirely. We are happy with our black Q7 logo and do not want to change it.
Our company address changed too. It is now 58 Corvallen, Irvine, CA 92741
Updates

It was reported by Sketch Harbor email today that the uploaded files didnt upload. I am trying again.

Target Market(s)

Architects and Building Owners (People making multi-million dollar decisions)

Industry/Entity Type

Consulting Engineering

Contact Information for Business Card

Contact info on the front. "wallpaper" design on back with tag line on the back "Engineering Your Future"

Font styles to use
Sans Serif

Requirements
Must have
• A vivid, modern, impactful ...but tasteful back of card design. It should communicate our premier status, but grab attention as innovative. DESIGN SHOULD BE ELEGANT AND NOT TOO BUSY.
Nice to have
• Repeating pattern, multi-color, something creative...
Should not have
• Anything that looks too playful or that we are not serious professionals. It should also not be too boring or conservative.

```html
<!DOCTYPE html>
<html lang="en">
<head>
<meta charset="utf-8">
<title>Q7 Business Card</title>
<link rel="stylesheet" href="https://fonts.googleapis.com/css2?family=Mulish:wght@600;700;800;900&display=swap">
<style>
  :root {
    --page: #ffffff;
    --card-black: #050709;
    --card-navy: #071521;
    --glow: #3fb4f2;
    --glow-soft: #1a6fa3;
    --line: #2e9be0;
    --white: #ffffff;
    --muted: #d7dde2;
  }
  * { box-sizing: border-box; margin: 0; padding: 0; }
  html, body {
    width: 1200px; height: 1200px; overflow: hidden;
    background: var(--page);
    font-family: "Mulish", Arial, sans-serif;
  }
  .board { position: relative; width: 1200px; height: 1200px; }
  .card {
    position: absolute; top: 52px; width: 518px; height: 334px;
    overflow: hidden; background: var(--card-black);
  }
  .card-back { left: 54px; }
  .card-front { left: 629px; }
  .card-art { position: absolute; inset: 0; width: 100%; height: 100%; }

  .brand-center {
    position: absolute; left: 50%; top: 50%;
    transform: translate(-50%, -50%);
    font-size: 92px; font-weight: 900; color: var(--white);
    letter-spacing: -2px; line-height: 1;
  }
  .brand-small {
    position: absolute; left: 46px; top: 38px;
    font-size: 40px; font-weight: 900; color: var(--white);
    letter-spacing: -1px; line-height: 1;
  }
  .identity { position: absolute; left: 50px; top: 190px; color: var(--white); }
  .identity .name { font-size: 21px; font-weight: 800; letter-spacing: 1.2px; }
  .identity .creds { font-size: 12.5px; font-weight: 800; letter-spacing: 0.6px; margin-top: 4px; }
  .identity .role { font-size: 15px; font-weight: 800; letter-spacing: 0.8px; margin-top: 2px; }
  .contact {
    position: absolute; left: 50px; bottom: 20px;
    font-size: 9.5px; font-weight: 800; line-height: 1.15; color: var(--muted);
  }
  .address {
    position: absolute; right: 58px; bottom: 20px; text-align: right;
    font-size: 9.5px; font-weight: 800; line-height: 1.15; color: var(--muted);
  }
</style>
</head>
<body>
<main class="board">

  <section class="card card-back" aria-label="Card back">
    <svg class="card-art" viewBox="0 0 518 334" role="img" aria-label="Dark blue backdrop with soft light glows and thin crossing lines">
      <defs>
        <linearGradient id="backBase" x1="0" y1="0" x2="1" y2="1">
          <stop offset="0" stop-color="#061018"/>
          <stop offset="0.5" stop-color="#0b2d47"/>
          <stop offset="1" stop-color="#061420"/>
        </linearGradient>
        <radialGradient id="haze" cx="0.55" cy="0.45" r="0.6">
          <stop offset="0" stop-color="#1c6ea6" stop-opacity="0.7"/>
          <stop offset="1" stop-color="#0a2436" stop-opacity="0"/>
        </radialGradient>
        <radialGradient id="flare">
          <stop offset="0" stop-color="#ffffff"/>
          <stop offset="0.12" stop-color="#9fe0ff"/>
          <stop offset="0.35" stop-color="#2f9fe4" stop-opacity="0.75"/>
          <stop offset="1" stop-color="#1a6fa3" stop-opacity="0"/>
        </radialGradient>
        <linearGradient id="sweep" x1="0" y1="0" x2="1" y2="0">
          <stop offset="0" stop-color="#2c8fd0" stop-opacity="0"/>
          <stop offset="0.5" stop-color="#2c8fd0" stop-opacity="0.45"/>
          <stop offset="1" stop-color="#2c8fd0" stop-opacity="0"/>
        </linearGradient>
      </defs>
      <rect width="518" height="334" fill="url(#backBase)"/>
      <rect width="518" height="334" fill="url(#haze)"/>
      <path d="M120 334 C170 270 260 250 380 262 L380 334 Z" fill="url(#sweep)"/>
      <line x1="72" y1="0" x2="72" y2="334" stroke="var(--line)" stroke-width="1.2" opacity="0.8"/>
      <line x1="433" y1="0" x2="433" y2="334" stroke="var(--line)" stroke-width="1.2" opacity="0.7"/>
      <line x1="0" y1="40" x2="518" y2="40" stroke="var(--line)" stroke-width="1" opacity="0.6"/>
      <line x1="0" y1="290" x2="300" y2="290" stroke="var(--line)" stroke-width="1" opacity="0.6"/>
      <circle cx="433" cy="40" r="70" fill="url(#flare)"/>
      <circle cx="72" cy="290" r="80" fill="url(#flare)"/>
    </svg>
    <div class="brand-center">Q7</div>
  </section>

  <section class="card card-front" aria-label="Card front">
    <svg class="card-art" viewBox="0 0 518 334" aria-hidden="true">
      <defs>
        <radialGradient id="sideGlow" cx="0.05" cy="0.55" r="0.55">
          <stop offset="0" stop-color="#1e6fa6" stop-opacity="0.65"/>
          <stop offset="1" stop-color="#050709" stop-opacity="0"/>
        </radialGradient>
        <linearGradient id="rightLine" x1="0" y1="0" x2="0" y2="1">
          <stop offset="0" stop-color="#2e9be0" stop-opacity="0"/>
          <stop offset="0.6" stop-color="#2e9be0" stop-opacity="0.7"/>
          <stop offset="1" stop-color="#2e9be0" stop-opacity="0.2"/>
        </linearGradient>
        <linearGradient id="baseLine" x1="0" y1="0" x2="1" y2="0">
          <stop offset="0" stop-color="#2e9be0" stop-opacity="0.5"/>
          <stop offset="1" stop-color="#2e9be0" stop-opacity="0"/>
        </linearGradient>
      </defs>
      <rect width="518" height="334" fill="url(#sideGlow)"/>
      <line x1="476" y1="60" x2="476" y2="334" stroke="url(#rightLine)" stroke-width="1.4"/>
      <line x1="0" y1="270" x2="240" y2="270" stroke="url(#baseLine)" stroke-width="1"/>
    </svg>
    <div class="brand-small">Q7</div>
    <div class="identity">
      <p class="name">ELIAS VARGA, PE</p>
      <p class="creds">HFDP, LEED AP</p>
      <p class="role">CEO/ PRINCIPAL</p>
    </div>
    <div class="contact">
      <p>(555) 014-7720</p>
      <p>elias.varga@q7eng.com</p>
      <p>q7eng.com</p>
    </div>
    <div class="address">
      <p>58 Corvallen</p>
      <p>Irvine</p>
      <p>CA 92741</p>
    </div>
  </section>

</main>
</body>
</html>
```